Broschüren-Design für Versicherungsagenten
Zielgruppe
Ich bin mit KL-Vorsorge als unabhängiger Versicherungsagent Selbstständig. (www.kl-vorsorge.de)
Ich habe mich auf die Absicherung von biometrischen Risiken spezialisiert - die auch in der Broschüre Thematisiert werden sollen. Das Oberthema der Broschüre ist 'biometrische Risiken'. Dies soll dann auf die Themen: Arbeitskraft, Langlebigkeit und Pflege heruntergebrochen werden.
Zielgruppe sind vor allem junge Menschen, die gerade erst eine Ausbildung gestartet oder ihr Studium beendet haben.
Aufgabenstellung
Das Design sollte die drei Hauptbereiche: Arbeitskraft, Langlebigkeit und Pflege, leicht verständlich dem Kunden veranschaulichen. Texte, Informationen und Grafiken (in der Reihenfolge, so wie ich mir das vorstelle) sind als Datei beigefügt.
Das ganze soll im DIN A4 Format gedruckt werden, wobei ich auf einen Hochwertigen Druck inklusive Druckveredelung hohen Wert lege.

```html
<!DOCTYPE html>
<html lang="de">
<head>
<meta charset="utf-8">
<title>KL-Vorsorge – Broschüre Biometrische Risiken</title>
<link rel="stylesheet" href="https://fonts.googleapis.com/css2?family=Open+Sans:wght@300;400;600;700&family=Roboto:wght@300;400;700&family=Tinos&display=swap">
<style>
:root{
  --teal:#13a199;
  --grey:#c6c6c8;
  --grey-mid:#b2b2b4;
  --grey-dark:#9c9c9e;
  --ink:#1d1d1b;
  --text:#4a4a4a;
  --red:#e2231a;
  --ice:#dcecf1;
  --paper:#ffffff;
  --page-shadow:0 4px 14px rgba(0,0,0,.28);
}
*{box-sizing:border-box;margin:0;padding:0}
html,body{width:1200px;height:2168px;overflow:hidden;background:var(--paper)}
body{position:relative;font-family:"Roboto",Arial,sans-serif;color:var(--text)}
.sheet{position:absolute;background:var(--paper);box-shadow:var(--page-shadow);overflow:hidden}
.spread-one{left:148px;top:112px;width:900px;height:636px}
.spread-two{left:148px;top:799px;width:894px;height:632px}
.back-cover{left:375px;top:1483px;width:446px;height:632px}
.fold{position:absolute;top:0;bottom:0;width:1px;background:#e4e4e4}
.abs{position:absolute}
.small{font-size:8px;line-height:1.35;font-weight:300;color:var(--text)}
.lead{font-family:"Open Sans",sans-serif;font-weight:300;color:var(--teal);font-size:24.5px;line-height:1.2}
.label-bold{font-weight:700;color:var(--ink)}
/* capital circles */
.years{position:absolute;width:52px;height:52px;border-radius:50%;background:var(--ink);color:#fff;text-align:center;font-family:"Roboto",sans-serif}
.years b{display:block;font-size:19px;line-height:1;margin-top:12px}
.years span{display:block;font-size:6px;letter-spacing:.5px}
.capital{position:absolute;width:128px;font-size:6.5px;text-align:center}
.capital h4{font-size:7px;font-weight:700;color:var(--ink);margin-bottom:5px}
.capital table{width:100%;border-collapse:collapse}
.capital th{background:var(--ink);color:#fff;font-weight:400;padding:2px 0}
.capital td{padding:3px 0;border-bottom:1px solid var(--ink);color:var(--ink)}
/* cost boxes */
.cost{position:absolute;background:var(--ice);font-family:"Tinos",serif;font-size:6px;color:var(--ink);padding:8px 6px;line-height:1.35}
.cost h5{font-size:6px;font-weight:700;margin-bottom:6px}
.cost .row{display:flex;justify-content:space-between}
.cost .sum{border-top:1px solid var(--ink);margin-top:10px;padding-top:4px}
.cost .total{display:inline-block;border:1px solid var(--red);border-radius:50%;padding:0 5px}
/* payer flow */
.step{position:absolute;left:27px;width:396px;border-radius:8px;text-align:center;font-size:5.5px;line-height:1.3;padding:5px 10px;color:var(--ink)}
.step h6{font-size:7px;font-weight:700;margin-bottom:2px}
.step::after{content:"";position:absolute;left:50%;bottom:-10px;margin-left:-22px;border-left:22px solid transparent;border-right:22px solid transparent;border-top:10px solid inherit}
.step.first{background:var(--grey-dark)}
.step.second{background:var(--grey-mid)}
.step.third{background:#d6d6d8}
.step.last{background:var(--red);color:#fff}
.arrow{position:absolute;left:203px;width:0;height:0;border-left:22px solid transparent;border-right:22px solid transparent}
</style>
</head>
<body>

<!-- Spread 1: Langlebigkeit / Pflege -->
<section class="sheet spread-one">
  <div class="fold" style="left:450px"></div>

  <div class="abs small" style="left:22px;top:22px;width:200px">
    <span class="label-bold" style="font-weight:400;color:var(--ink)">Rechnung:</span><br>
    Angenommen Sie investieren über 20, 30 und 40 Jahre hinweg einen Monatsbeitrag von 100 Euro in Ihre private Altersvorsorge.
  </div>

  <svg class="abs" style="left:18px;top:100px" width="210" height="112" viewBox="0 0 210 112" role="img" aria-label="Liniendiagramm Kapitalentwicklung">
    <g font-size="5" fill="#555" font-family="Roboto,sans-serif">
      <text x="0" y="14">500.000 €</text><text x="0" y="31">400.000 €</text><text x="0" y="48">300.000 €</text>
      <text x="0" y="65">200.000 €</text><text x="0" y="82">100.000 €</text><text x="12" y="99">0 €</text>
      <text x="72" y="109">3%</text><text x="128" y="109">6%</text><text x="182" y="109">9%</text>
    </g>
    <g stroke="#ddd" stroke-width=".6">
      <line x1="30" y1="12" x2="195" y2="12"/><line x1="30" y1="29" x2="195" y2="29"/><line x1="30" y1="46" x2="195" y2="46"/>
      <line x1="30" y1="63" x2="195" y2="63"/><line x1="30" y1="80" x2="195" y2="80"/><line x1="30" y1="97" x2="195" y2="97"/>
    </g>
    <polyline points="36,97 76,92 132,90 186,86" fill="none" stroke="#3a84c9" stroke-width="1.2"/>
    <polyline points="36,97 76,88 132,79 186,68" fill="none" stroke="#5aa33a" stroke-width="1.2"/>
    <polyline points="36,97 76,83 132,64 186,23" fill="none" stroke="#f6b51c" stroke-width="1.2"/>
    <g font-size="5" fill="#555"><rect x="84" y="16" width="4" height="4" fill="#3a84c9"/><text x="91" y="20">20 Jahre</text>
      <rect x="84" y="23" width="4" height="4" fill="#5aa33a"/><text x="91" y="27">30 Jahre</text>
      <rect x="84" y="30" width="4" height="4" fill="#f6b51c"/><text x="91" y="34">40 Jahre</text></g>
  </svg>

  <div class="years" style="left:61px;top:236px"><b>20</b><span>JAHRE</span></div>
  <div class="years" style="left:195px;top:235px"><b>30</b><span>JAHRE</span></div>
  <div class="years" style="left:334px;top:235px"><b>40</b><span>JAHRE</span></div>

  <div class="capital" style="left:24px;top:295px"><h4>Kapital nach 20 Jahren</h4>
    <table><tr><th>3 %</th><th>6 %</th><th>9 %</th></tr><tr><td>32.768 €</td><td>45.565 €</td><td>64.849 €</td></tr></table></div>
  <div class="capital" style="left:160px;top:295px"><h4>Kapital nach 30 Jahren</h4>
    <table><tr><th>3 %</th><th>6 %</th><th>9 %</th></tr><tr><td>58.014 €</td><td>97.926 €</td><td>171.436 €</td></tr></table></div>
  <div class="capital" style="left:298px;top:295px"><h4>Kapital nach 40 Jahren</h4>
    <table><tr><th>3 %</th><th>6 %</th><th>9 %</th></tr><tr><td>91.246 €</td><td>191.699 €</td><td>424.985 €</td></tr></table></div>

  <p class="abs small" style="left:22px;top:363px;width:160px">Die Zahlung einer lebenslangen Rente ist die einzige Möglichkeit, das Langlebigkeitsrisiko abzusichern.</p>
  <p class="abs small" style="left:233px;top:363px;width:170px">Andere Produkte leisten das nicht. Investmentprodukte mit Auszahlungsplan oder Sparguthaben zum Beispiel enden zu einem bestimmten Zeitpunkt.</p>

  <p class="abs lead" style="left:22px;top:423px;width:420px">Wir arbeiten zusammen mit Ihnen ein individuelles Vorsorgekonzept aus, um die richtigen Weichen so früh wie möglich zu stellen.</p>

  <svg class="abs" style="left:0;top:0" width="900" height="636" viewBox="0 0 900 636">
    <polygon points="0,636 450,514 450,636" fill="var(--teal)"/>
    <rect x="451" y="513" width="449" height="123" fill="var(--teal)"/>
    <circle cx="715" cy="172" r="194" fill="var(--teal)"/>
    <circle cx="729" cy="168" r="192" fill="var(--grey)"/>
    <circle cx="574" cy="347" r="80" fill="var(--teal)"/>
  </svg>

  <div class="abs" style="left:680px;top:17px;width:210px;color:#fff">
    <h2 style="font-family:'Open Sans',sans-serif;font-weight:300;color:var(--teal);font-size:24px;line-height:1">Pflege</h2>
    <p class="small" style="color:var(--teal)">„Können Sie sich alt werden auch finanziell leisten?“</p>
    <p class="small" style="color:#fff;margin-top:10px">Die Menschen in Deutschland werden immer älter. Das ist schön. Doch Sie werden auch immer pflegebedürftiger. Das ist weniger schön und macht private Vorsorge notwendiger denn je.</p>
    <p class="small" style="color:var(--teal);font-weight:700;margin-top:18px">Wer auf die Risiken eines Pflegefalls nicht vorbereitet ist, gerät schnell in eine finanzielle Schieflage.</p>
    <p class="small" style="color:#fff;margin-top:14px">Staatliche Versorgung – Teilkasko im Pflegefall</p>
    <p class="small" style="color:#fff;margin-top:8px">1995 wurde vom Gesetzgeber die staatliche Pflegepflichtversicherung ins Leben gerufen. 2017 fand dazu eine grundlegende Reform statt, unter anderem wurde die Pflegebedürftigkeit mit fünf Pflegegraden neu definiert. Der Pflegegrad ergibt sich aus einem Punktesystem und basiert auf sechs relevante Kategorien.</p>
  </div>

  <p class="abs" style="left:502px;top:293px;width:144px;text-align:center;color:#fff;font-family:'Open Sans',sans-serif;font-weight:300;font-size:11px;line-height:1.3"><span style="font-weight:400">25 Menschen</span><br>unter 65 Jahren, werden in Deutschland jeden Tag zum Pflegefall, beispielsweise durch Unfälle oder Krankheiten.</p>

  <div class="abs small" style="left:472px;top:443px;width:210px">
    <span style="font-weight:400;color:var(--ink)">Können Sie sich das leisten?</span><br>
    Die Kosten für Pflege sind einzig und allein von einer Frage abhängig: Wie und auf welchem Niveau möchten Sie persönlich gepflegt und betreut werden?
  </div>

  <div class="cost" style="left:469px;top:519px;width:172px;height:97px">
    <h5>Beispiel: Monatlicher Eigenanteil im hochwertigen Pflegeheim für Pflegegrad 3</h5>
    <div class="row"><span>Einheitlicher Eigenanteil an Pflegekosten</span><span>1.135 €</span></div>
    <div class="row"><span>Unterkunft/Verpflegung</span><span>801 €</span></div>
    <div class="row"><span>Investitionskosten</span><span>399 €</span></div>
    <div class="row sum"><span>Eigenanteil</span><span>2.335 €</span></div>
    <div class="row"><span>Eigenanteil nach 7 Jahren</span><span class="total">196.140 €</span></div>
  </div>
  <div class="cost" style="left:675px;top:522px;width:168px;height:93px">
    <h5>Beispiel: Monatlicher Eigenanteil im durchschnittlichen Pflegeheim für Pflegegrad 3</h5>
    <div class="row"><span>Einheitlicher Eigenanteil an Pflegekosten</span><span>555 €</span></div>
    <div class="row"><span>Unterkunft/Verpflegung</span><span>861 €</span></div>
    <div class="row"><span>Investitionskosten</span><span>406 €</span></div>
    <div class="row sum"><span>Eigenanteil</span><span>1.822 €</span></div>
    <div class="row"><span>Eigenanteil nach 7 Jahren</span><span class="total">153.048 €</span></div>
  </div>
</section>

<!-- Spread 2: Wer zahlt? / Kontakt -->
<section class="sheet spread-two">
  <div class="fold" style="left:447px"></div>

  <div class="abs" style="left:24px;top:27px;width:400px;text-align:center;color:var(--ink);font-size:7.5px;font-weight:700;line-height:1.6">
    <p style="font-size:8px">Wer zahlt?</p>
    <p>Egal ob Sie später zu Hause oder in einem Pflegeheim gepflegt werden,<br>den Großteil der Kosten müssen Sie selbst tragen.</p>
  </div>

  <div class="arrow" style="top:131px;border-top:12px solid var(--grey-dark)"></div>
  <div class="step first" style="top:95px;height:37px"><h6>ZUERST: DER PFLEGEBEDÜRFTIGE</h6>Zur Finanzierung im Pflegefall werden erst Ihre eigenen Einkünfte wie Gehalt oder Rente sowie Ihr Gesamtvermögen wie z.B. Eigenheim, Immobilien und Erspartes herangezogen. Auch wenn man das lieber den Kindern vererbt hätte.</div>
  <div class="arrow" style="top:178px;border-top:12px solid var(--grey-mid)"></div>
  <div class="step second" style="top:150px;height:29px"><h6>DANN: DER EHEPARTNER</h6>Sollten diese nicht ausreichen, werden die Einkünfte und das Vermögen des Ehepartners bzw. des Lebenspartners herangezogen.</div>
  <div class="step third" style="top:201px;height:32px"><h6>ANSCHLIESSEND: DIE KINDER</h6>Kann auch Ihr Ehepartner den entsprechenden Eigenanteil der Pflegekosten nicht übernehmen, kommen Ihre Kinder für diese Kosten auf.</div>
  <div class="step last" style="top:253px;height:45px"><h6>ZUM SCHLUSS: DAS SOZIALAMT</h6>Sollte das nicht reichen, müssen Sie als Erstes selbst „Sozialhilfe“ beantragen. Der Staat kommt erst für die Pflegekosten auf, wenn alle anderen Möglichkeiten ausgeschöpft sind. Die erbrachten Leistungen kann der Staat zudem nachträglich von den Kindern zurückfordern.</div>

  <h2 class="abs lead" style="left:22px;top:315px">Vollkasko nur<br>mit Pflegezusatz</h2>
  <div class="abs small" style="left:22px;top:382px;width:400px">
    - Einkommens- und Kostenabsicherung im Pflegefall<br>
    - Schutz vor Verlust des angesammelten Vermögens<br>
    - Schutz von nahen Angehörigen vor finanziellen und logistischen Folgen (§ 1601 BGB)<br>
    - Erbschaftssicherung<br>
    - Menschenwürdiges und bedarfsgerechtes Pflegeumfeld ermöglichen
  </div>
  <div class="abs small" style="left:22px;top:449px;width:260px">
    <span style="font-weight:700;color:var(--ink)">Eines bleibt aber gleich:</span><br>
    Die gesetzliche Pflegeversicherung sorgt weiterhin<br>NUR für die minimale Grundsicherung.
  </div>
  <p class="abs lead" style="left:22px;top:505px;width:420px">Wir helfen Ihnen dabei gezielt diese Lücken zu schließen indem wir mit Ihnen ein individuelles Vorsorgekonzept ausarbeiten.</p>

  <div class="abs small" style="left:470px;top:20px;width:212px">
    <p>Die meisten Menschen sind sich der herrschenden Probleme der fehlenden Absicherung der Arbeitskraft, der Altersarmut und des Pflegenotstands sehr wohl bewusst. Allerdings mangelt es noch an Handlungen.</p>
    <p style="margin-top:10px">Dies liegt sehr oft daran, dass der Ansprechpartner/Problemlöser in diesem Bereich fehlt.</p>
    <p style="margin-top:10px">Genau da stellen wir uns auf. Es ist Aufgabe des Vermittlers, Angebote in den Bedingungen &amp; den Tarifen zu überprüfen und zu gewährleisten.</p>
  </div>

  <svg class="abs" style="left:447px;top:0" width="447" height="632" viewBox="447 0 447 632">
    <circle cx="738" cy="498" r="227" fill="var(--teal)"/>
    <circle cx="748" cy="504" r="225" fill="var(--grey)"/>
    <circle cx="746" cy="228" r="92" fill="var(--teal)"/>
  </svg>

  <p class="abs" style="left:676px;top:197px;width:150px;color:#fff;font-size:8px;font-weight:700;line-height:1.3">Du hast Fragen zu meiner Arbeit?<br>Oder Unklarheiten zu einer bestimmten Versicherung?<br>Melde dich bei mir!</p>

  <p class="abs" style="left:674px;top:358px;width:215px;color:#fff;font-family:'Open Sans',sans-serif;font-weight:300;font-size:24.5px;line-height:1.2">Wir stehen für:<br>TOP Bedingungen<br>den besten<br>Versicherungs-<br>schutz</p>
</section>

<!-- Rückseite -->
<section class="sheet back-cover">
  <svg class="abs" style="left:0;top:0" width="446" height="632" viewBox="0 0 446 632">
    <circle cx="500" cy="190" r="468" fill="var(--grey)"/>
    <circle cx="510" cy="170" r="468" fill="var(--teal)"/>
    <circle cx="515" cy="150" r="468" fill="var(--grey)"/>
    <circle cx="520" cy="130" r="468" fill="var(--teal)"/>
    <rect x="0" y="0" width="446" height="122" fill="var(--teal)"/>
  </svg>
  <address class="abs small" style="left:234px;top:62px;font-style:normal;color:#e6f5f4;line-height:1.4">
    Belwig Max<br>Lindenstraße 4<br>89312 Günzburg<br>Telefon: 08221 5550142<br>Mobil: 0151 5550187<br>E-Mail: maxbelwig@kl-vorsorge.de
  </address>
</section>

</body>
</html>
```